Nitrogen generation business website

Project Overview:
This project aims to create a sleek, user-friendly, and responsive WordPress template for Kelbo4, a provider of Nitrogen generation solutions. The site will serve as a primary touchpoint for customers and businesses looking to enquire about or purchase Kelbo4 products and services. The website should clearly communicate the benefits of working with Kelbo4 as a distributor, focusing on ease of access, expert consultation, and fast, reliable service.
Target Audience:
• Industrial companies seeking Nitrogen solutions.
• Engineers, facility managers, and purchasing teams in need of high-quality Nitrogen systems.
• Partners or businesses seeking to collaborate or purchase through a distributor.
Key Objectives:
1. Establish Kelbo4’s Brand Identity: Use the bold, energetic logo and branding of Kelbo4 (as seen in the uploaded logo) throughout the design. Ensure the brand’s personality shines, with a focus on modernity, reliability, and innovation.
2. Showcase Products and Solutions: Display detailed product categories and descriptions, emphasising the solutions Kelbo4 offers.
3. Lead Generation: Incorporate contact forms, quote requests, and easy-to-find CTAs to convert visitors into leads.
4. User-Centric Design: The design must be intuitive and user-friendly, providing a smooth experience across desktop and mobile devices.
Design Requirements:
1. Home Page:
• Hero Banner: A dynamic, visually engaging hero banner featuring air and gas purification systems, paired with strong CTAs like “Request a Quote” or “Contact Us for Solutions.” The banner should align with the vibrant red and yellow tones in the Kelbo4 logo.
• Key Product Categories: Introduce the main product categories with icons or images linked to individual product pages.
• Kelbo4 Expertise Section: A section emphasising the company’s role as a trusted distributor, backed by experience and a strong partnership network.
• Why Choose Kelbo4: Highlight 3-4 major benefits, such as “Quick Delivery,” “Expert Consultation,” and “Innovative Technology.”
• Client Testimonials/Partners: Space for customer feedback, testimonials, or logos of partner companies to build trust.
• Newsletter or Enquiry Form: Place a compact form for capturing visitor details for quotes, enquiries, or subscriptions.
2. Product Pages:
• Category Pages: Create well-structured product category pages (e.g., Air Filtration Systems, Nitrogen Generators) similar to industry-standard designs. Each category page should feature professional imagery, short product descriptions, and links to detail pages.
• Product Detail Pages: Each product page will contain:
• High-quality images of the product.
• Detailed specifications, technical descriptions, and features.
• Options to download datasheets or brochures (PDF format).
• Clear CTAs to request a quote or contact sales.
• Product Comparison Tool (Optional): Allow users to compare multiple products, emphasising key features and specifications.
3. About Kelbo4 Page:
• Provide an overview of Kelbo4’s history, mission, and the value it provides as a leading distributor.
• Highlight industry expertise, the partnership network, and any accolades or certifications.
• Mention any regional advantages or special services (e.g., fast delivery times, on-site consultation).
4. Contact Us Page:
• Clean and Simple Form: Include fields for general inquiries or specific product requests.
• Contact Information: Display the company’s, email address info@kelbo4.co.uk.
5. Additional Functionalities:
• Responsive Design: Ensure the design is fully responsive, optimised for mobile, tablet, and desktop viewing.
• SEO Optimisation: Include best practices for search engine optimization (SEO), including clean URLs, meta tags, and image alt text.
• Fast Loading Speed: Optimise images, scripts, and code for fast loading times to improve user experience.
• Social Media Integration: Provide links to social media profiles (if applicable) and potentially include a feed for recent updates.
• Optional Blog: Create a blog space for sharing industry news, product updates, or educational content to engage with visitors and improve SEO.
Style Guide:
1. Color Palette:
• Use colors consistent with the Kelbo4 logo: Red (#FF0000) and Yellow (#FFD700) as primary colors. Incorporate neutral colors (such as white, gray, or black) for balance and readability.
• Accent colors may be introduced for subtle highlights, but the focus should be on the bold, energetic color scheme of Kelbo4.
2. Typography:
• Primary Font for Headings: A bold, modern sans-serif font that complements the strong branding of Kelbo4.
• Secondary Font for Body Text: Clean, easy-to-read sans-serif or serif font for optimal readability across devices.
• Typography Emphasis: Use large, bold typography for headlines to match the boldness of the logo and brand identity.
3. Imagery:
• Use high-quality industrial and technical imagery that reflects the air and gas purification products Kelbo4 distributes.
• Incorporate imagery showing products in action, e.g., in industrial settings or installations.
• Avoid clutter; ensure images are used to enhance user understanding, not overwhelm.
4. Icons:
• Utilise modern, flat-style icons that align with the clean and professional image of Kelbo4. Icons could represent services such as “Fast Delivery,” “Expert Support,” and “High-Quality Products.”
Functionality Requirements:
1. Content Management System (CMS): Build the site using WordPress for easy content management, allowing Kelbo4 staff to update content, product information, and blog posts.
2. Quote Request Integration: Ensure the site has a functional and easy-to-access “Request a Quote” form that appears on every product and service page.
3. Customer Support Section: Optionally include a section for FAQs, product guides, or a knowledge base to support customers and prospects.
4. Security: Implement SSL encryption and ensure that other security best practices (e.g., spam prevention for forms) are followed.
5. Multilingual Support (Optional): Provide the option to support multiple languages, depending on the regional scope of Kelbo4’s distribution services.
Deliverables:
• WordPress template with a homepage, product pages, about section, and contact page.
• SEO-friendly and responsive design.
• Clear CTAs for lead generation (e.g., “Request a Quote”).
• User-friendly interface for both desktop and mobile devices.
Inspiration/Competitors:
• Competitor Analysis: Research similar distributors in the air and gas purification industry for design inspiration.
• Brand Consistency: Ensure Kelbo4’s bold branding is prominent and differentiates it from competitors.
Food & Beverage manufacturers, Laser Cutting, Electronics manufacturers, General Industrial Manufacturers

```html
<!DOCTYPE html>
<html lang="en">
<head>
<meta charset="utf-8">
<title>Kelbo4 — Nitrogen Generation Solutions</title>
<link href="https://fonts.googleapis.com/css2?family=Montserrat:wght@600;700;800&family=Lato:wght@400;700&family=Roboto:wght@400;700&display=swap" rel="stylesheet">
<style>
:root{
  --red:#f11c1c;
  --red-deep:#e52222;
  --yellow:#fdbf0f;
  --gold:#e9b40b;
  --ink:#111111;
  --dark:#0a0a0a;
  --white:#ffffff;
  --grey:#6b6b6b;
  --field:#ffffff;
}
*{margin:0;padding:0;box-sizing:border-box}
html,body{width:1200px;height:3756px;overflow:hidden}
body{position:relative;background:var(--white);font-family:'Lato',sans-serif;color:var(--ink)}
.abs{position:absolute}
.heading{font-family:'Montserrat',sans-serif;font-weight:700}
.btn{position:absolute;display:flex;align-items:center;justify-content:center;font-family:'Montserrat',sans-serif;font-weight:700;font-size:16px;border-radius:2px}
.btn-yellow{background:var(--yellow);color:var(--white)}
.btn-red{background:var(--red);color:var(--white)}
.btn-white{background:var(--white);color:var(--red)}

/* header */
.topline{top:0;left:0;width:1200px;height:4px;background:var(--red)}
.site-header{top:4px;left:0;width:1200px;height:85px;background:var(--white)}
.brand{font-family:'Montserrat',sans-serif;font-weight:800;font-size:40px;color:var(--red)}
.nav a{position:absolute;top:34px;font-size:16px;color:#333;text-decoration:none}
.nav a.active{color:var(--red);font-weight:700;text-decoration:underline}

/* hero */
.hero{top:89px;left:0;width:1200px;height:599px;background:linear-gradient(135deg,#1c2430 0%,#2c2a28 45%,#1b2536 100%)}
.hero-title{left:111px;top:225px;font-size:64px;line-height:70px;color:var(--white);font-weight:800}
.hero-text{left:111px;top:375px;width:360px;font-size:15.5px;line-height:31px;color:var(--white)}

/* why */
.section-title{width:1200px;left:0;text-align:center;font-size:36px}
.section-title .r{color:var(--red)} .section-title .y{color:var(--yellow)}
.feature-label{width:300px;text-align:center;font-family:'Montserrat',sans-serif;font-weight:500;font-size:21px;color:var(--ink)}

/* expertise */
.expertise{top:1088px;left:0;width:1200px;height:538px;background:linear-gradient(100deg,#ea2424,#f23030 60%,#e82a2a)}
.expertise-title{left:623px;top:1170px;font-size:34px;color:var(--white)}
.expertise-text{left:623px;top:1229px;width:450px;font-size:15px;line-height:31px;color:var(--white)}

/* products */
.card-img{border-radius:0 0 60px 0}
.card-label{font-family:'Montserrat',sans-serif;font-weight:700;font-size:17px;text-align:center;width:309px}

/* testimonials */
.testimonials{top:2258px;left:0;width:1200px;height:543px;background:linear-gradient(180deg,#f0bb07,#e4b40c)}
.t-card{width:310px;height:328px;top:2391px;border:3px solid var(--white);border-radius:10px}
.stars{position:absolute;left:24px;top:26px;color:var(--white);font-size:15px;letter-spacing:3px}
.t-text{position:absolute;left:24px;top:54px;width:258px;font-family:'Roboto',sans-serif;font-size:14px;line-height:25.5px;color:var(--white);text-align:justify}
.t-rule{position:absolute;left:24px;top:212px;width:258px;height:1px;background:rgba(255,255,255,.6)}
.avatar{position:absolute;left:24px;top:240px;width:56px;height:56px;border-radius:50%;background:linear-gradient(160deg,#c9b9a6,#7d6a5a)}
.t-name{position:absolute;left:96px;top:244px;font-family:'Roboto',sans-serif;font-weight:700;font-size:18px;color:var(--white)}
.t-place{position:absolute;left:96px;top:272px;font-family:'Roboto',sans-serif;font-size:14px;color:rgba(255,255,255,.85)}
.arrow{width:38px;height:38px;border-radius:50%;background:var(--white);border:1px solid #ddd;display:flex;align-items:center;justify-content:center}

/* contact */
.field{background:var(--field);box-shadow:0 2px 10px rgba(0,0,0,.12);border-radius:4px;font-size:14px;color:#555;padding:16px 17px}

/* footer */
.site-footer{top:3330px;left:0;width:1200px;height:426px;background:var(--dark)}
.f-title{font-family:'Montserrat',sans-serif;font-weight:700;font-size:21px;color:var(--white)}
.f-link{font-size:15px;color:var(--white);display:flex;align-items:center;gap:12px}
.social{width:24px;height:24px;border-radius:50%;background:var(--red)}
.f-icon{width:38px;height:38px;border-radius:50%;background:var(--red);display:flex;align-items:center;justify-content:center}
.f-text{font-size:15px;color:var(--white)}
</style>
</head>
<body>

<div class="abs topline"></div>
<header class="abs site-header">
  <div class="abs brand" style="left:112px;top:16px">Kelbo4</div>
  <nav class="nav">
    <a class="active" style="left:435px">Home</a>
    <a style="left:519px">About</a>
    <a style="left:604px">Product</a>
    <a style="left:701px">Services</a>
    <a style="left:802px">Contact Us</a>
  </nav>
  <div class="btn btn-yellow" style="left:916px;top:19px;width:172px;height:46px;box-shadow:0 3px 8px rgba(0,0,0,.2)">Request a Quote</div>
</header>

<section class="abs hero" role="img" aria-label="Night aerial view of an industrial port with storage tanks"></section>
<h1 class="abs heading hero-title">Welcome To<br>Kelbo4</h1>
<p class="abs hero-text">Kelbo4 specialises in supplying, installing, and servicing nitrogen generators for efficient on-site nitrogen production.</p>
<div class="btn btn-yellow" style="left:111px;top:484px;width:173px;height:47px">Request a Quote</div>
<svg class="abs" style="left:600px;top:170px" width="460" height="450">
  <circle cx="231" cy="224" r="219" fill="var(--yellow)"/>
  <circle cx="243" cy="224" r="206" fill="#fff"/>
</svg>
<div class="abs" role="img" aria-label="Compact grey nitrogen generator unit" style="left:720px;top:190px;width:250px;height:380px;border-radius:18px;background:linear-gradient(90deg,#c9cbcd,#eef0f1 50%,#a9acaf)"></div>

<h2 class="abs heading section-title" style="top:754px"><span class="r">Why Choose</span> <span class="y">Kelbo4</span></h2>
<svg class="abs" style="left:200px;top:840px" width="800" height="140">
  <g transform="translate(73,67)">
    <circle cx="-8" cy="-6" r="62" fill="#fff" stroke="var(--red)" stroke-width="2"/>
    <circle cx="0" cy="0" r="62" fill="var(--red)"/>
    <g fill="none" stroke="#fff" stroke-width="2.5"><rect x="-18" y="-12" width="24" height="20" rx="2"/><path d="M6 -6h9l8 8v6H6"/><circle cx="-10" cy="12" r="4"/><circle cx="14" cy="12" r="4"/><path d="M-26 -6h-8M-24 0h-10M-26 6h-6"/></g>
  </g>
  <g transform="translate(351,67)">
    <circle cx="-8" cy="-6" r="62" fill="#fff" stroke="var(--yellow)" stroke-width="2"/>
    <circle cx="0" cy="0" r="62" fill="var(--yellow)"/>
    <g fill="none" stroke="#fff" stroke-width="2.5"><circle cx="0" cy="-12" r="8"/><path d="M-4 -2v5h8v-5"/><circle cx="-16" cy="6" r="5"/><circle cx="16" cy="6" r="5"/><path d="M-26 22c0-8 6-11 10-11s10 3 10 11M6 22c0-8 6-11 10-11s10 3 10 11M-28 22h56"/></g>
  </g>
  <g transform="translate(685,67)">
    <circle cx="-8" cy="-6" r="62" fill="#fff" stroke="var(--red)" stroke-width="2"/>
    <circle cx="0" cy="0" r="62" fill="var(--red)"/>
    <g fill="none" stroke="#fff" stroke-width="2.5"><path d="M-10 14c-10-6-14-14-14-22a24 24 0 0 1 48 0c0 8-4 16-14 22z"/><path d="M-8 20h16M-6 26h12"/><circle cx="0" cy="-6" r="7"/></g>
  </g>
</svg>
<div class="abs feature-label" style="left:123px;top:983px">Quick Delivery</div>
<div class="abs feature-label" style="left:401px;top:983px">Expert Consultation</div>
<div class="abs feature-label" style="left:735px;top:983px">Innovative Technology</div>

<section class="abs expertise"></section>
<div class="abs" style="left:154px;top:1156px;width:400px;height:400px;border-radius:50%;background:#fff"></div>
<div class="abs" role="img" aria-label="Oil refinery with pipelines at sunset" style="left:162px;top:1164px;width:384px;height:384px;border-radius:50%;background:linear-gradient(180deg,#3e4e6e 0%,#c9785a 50%,#f0a45e 60%,#6e3e34 100%)"></div>
<h2 class="abs heading expertise-title">Kelbo4 Expertise</h2>
<p class="abs expertise-text">Kelbo4 specialises in supplying, installing, and servicing nitrogen generators for efficient on-site nitrogen production. Enhance your operations with our reliable, cost-effective nitrogen solutions. Discover how our advanced nitrogen generators can optimise your business today. Contact Kelbo4 for expert nitrogen generation services.Discover how our advanced nitrogen generators can optimise your business today. Contact Kelbo4 for expert nitrogen generation services.</p>
<div class="btn btn-white" style="left:623px;top:1489px;width:172px;height:46px">Request a Quote</div>

<h2 class="abs heading section-title" style="top:1706px"><span class="r">Product</span> <span class="y">Categories</span></h2>
<div class="abs card-img" role="img" aria-label="Rooftop air handling units" style="left:111px;top:1780px;width:309px;height:264px;background:linear-gradient(160deg,#9aa2a8,#d7dadc 50%,#7b8389)"></div>
<div class="abs card-img" role="img" aria-label="Engineers inspecting nitrogen storage tanks" style="left:446px;top:1780px;width:308px;height:264px;background:linear-gradient(160deg,#e6e4df,#b9b6ae 50%,#3d4a6a)"></div>
<div class="abs card-img" role="img" aria-label="Technician holding a pre-treatment filter" style="left:780px;top:1780px;width:308px;height:264px;background:linear-gradient(160deg,#cfd8c6,#2d3f8c 55%,#1c2660)"></div>
<div class="abs card-label" style="left:92px;top:2072px">Air Filtration Systems</div>
<div class="abs card-label" style="left:444px;top:2072px">Nitrogen Generators</div>
<div class="abs card-label" style="left:780px;top:2072px">Pre-Treatment</div>
<div class="btn btn-red" style="left:503px;top:2134px;width:194px;height:47px;box-shadow:0 3px 8px rgba(0,0,0,.2)">View More Products</div>

<section class="abs testimonials"></section>
<h2 class="abs heading section-title" style="top:2324px;color:#fff;font-size:32px">Testimonials</h2>
<div class="abs arrow" style="left:36px;top:2553px"><svg width="12" height="12"><path d="M8 1L3 6l5 5" stroke="#555" stroke-width="1.6" fill="none"/></svg></div>
<div class="abs arrow" style="left:1126px;top:2553px"><svg width="12" height="12"><path d="M4 1l5 5-5 5" stroke="#555" stroke-width="1.6" fill="none"/></svg></div>

<article class="abs t-card" style="left:105px">
  <div class="stars">★★★★★</div>
  <p class="t-text">Lorem ipsum dolor sit amet, consectetur adipiscing elit, sed do eiusmod tempor incididunt ut labore et dolore magna aliqua ut enim ad minim veniam, quis nostrud exercitation ullamco.</p>
  <div class="t-rule"></div><div class="avatar" role="img" aria-label="Customer portrait"></div>
  <div class="t-name">Dana Reyes</div><div class="t-place">Florida, United States</div>
</article>
<article class="abs t-card" style="left:440px">
  <div class="stars">★★★★★</div>
  <p class="t-text">Lorem ipsum dolor sit amet, consectetur adipiscing elit, sed do eiusmod tempor incididunt ut labore et dolore magna aliqua ut enim ad minim veniam, quis nostrud exercitation ullamco.</p>
  <div class="t-rule"></div><div class="avatar" role="img" aria-label="Customer portrait"></div>
  <div class="t-name">Dana Reyes</div><div class="t-place">Florida, United States</div>
</article>
<article class="abs t-card" style="left:777px">
  <div class="stars">★★★★★</div>
  <p class="t-text">Lorem ipsum dolor sit amet, consectetur adipiscing elit, sed do eiusmod tempor incididunt ut labore et dolore magna aliqua ut enim ad minim veniam, quis nostrud exercitation ullamco.</p>
  <div class="t-rule"></div><div class="avatar" role="img" aria-label="Customer portrait"></div>
  <div class="t-name">Dana Reyes</div><div class="t-place">Florida, United States</div>
</article>

<h2 class="abs heading section-title" style="top:2890px;font-size:32px">Contact Us</h2>
<div class="abs field" style="left:181px;top:2955px;width:411px;height:49px">Name</div>
<div class="abs field" style="left:605px;top:2955px;width:411px;height:49px">Email</div>
<div class="abs field" style="left:181px;top:3018px;width:411px;height:48px">Phone Number</div>
<div class="abs field" style="left:605px;top:3018px;width:411px;height:48px">Subject</div>
<div class="abs field" style="left:181px;top:3081px;width:835px;height:85px">Message</div>
<div class="btn btn-red" style="left:531px;top:3190px;width:137px;height:50px">Submit</div>

<footer class="abs site-footer"></footer>
<div class="abs brand" style="left:76px;top:3414px">Kelbo4</div>
<div class="abs social" style="left:84px;top:3495px"></div>
<div class="abs social" style="left:122px;top:3495px"></div>
<div class="abs social" style="left:160px;top:3495px"></div>
<div class="abs social" style="left:199px;top:3495px"></div>

<div class="abs f-title" style="left:296px;top:3390px">Other Links</div>
<div class="abs" style="left:296px;top:3427px;display:flex;flex-direction:column;gap:10px">
  <div class="f-link"><svg width="14" height="12"><path d="M0 6h10M6 1l5 5-5 5" stroke="#fff" stroke-width="2.4" fill="none"/></svg>FAQ</div>
  <div class="f-link"><svg width="14" height="12"><path d="M0 6h10M6 1l5 5-5 5" stroke="#fff" stroke-width="2.4" fill="none"/></svg>Terms of Use</div>
  <div class="f-link"><svg width="14" height="12"><path d="M0 6h10M6 1l5 5-5 5" stroke="#fff" stroke-width="2.4" fill="none"/></svg>Privacy Policy</div>
  <div class="f-link"><svg width="14" height="12"><path d="M0 6h10M6 1l5 5-5 5" stroke="#fff" stroke-width="2.4" fill="none"/></svg>Blog</div>
  <div class="f-link"><svg width="14" height="12"><path d="M0 6h10M6 1l5 5-5 5" stroke="#fff" stroke-width="2.4" fill="none"/></svg>Conditions</div>
</div>

<div class="abs f-title" style="left:507px;top:3390px">Contact Us</div>
<div class="abs f-icon" style="left:507px;top:3438px"><svg width="16" height="18"><path d="M8 17s6-6 6-10A6 6 0 0 0 2 7c0 4 6 10 6 10z" fill="#fff"/><circle cx="8" cy="7" r="2.2" fill="var(--red)"/></svg></div>
<div class="abs f-text" style="left:556px;top:3447px">Company Name,United State.</div>
<div class="abs f-icon" style="left:507px;top:3498px"><svg width="16" height="12"><rect width="16" height="12" rx="1.5" fill="#fff"/><path d="M1 1l7 6 7-6" stroke="var(--red)" stroke-width="1.4" fill="none"/></svg></div>
<div class="abs f-text" style="left:556px;top:3507px">info@kelbo4.co.uk</div>
<div class="abs f-icon" style="left:507px;top:3558px"><svg width="16" height="16"><path d="M3 1l3 0 1.5 4-2 1.3a9 9 0 0 0 4.2 4.2L11 8.5l4 1.5v3a2 2 0 0 1-2 2A13 13 0 0 1 1 3a2 2 0 0 1 2-2z" fill="#fff"/></svg></div>
<div class="abs f-text" style="left:556px;top:3567px">+1800 555 0142</div>

<div class="abs f-title" style="left:828px;top:3390px">Sign Up To Our Newsletter</div>
<p class="abs f-text" style="left:828px;top:3440px;width:290px;line-height:31px">Lorem ipsum dolor sit amet,consectetur adipiscing elit,adipiscing elit.</p>
<div class="abs f-text" style="left:831px;top:3510px">Email</div>
<div class="abs" style="left:830px;top:3540px;width:271px;height:1px;background:#fff"></div>
<div class="btn btn-red" style="left:835px;top:3571px;width:146px;height:51px;border-radius:26px;font-size:18px">Subscribe</div>

<div class="abs" style="left:99px;top:3695px;width:1002px;height:1px;background:#888"></div>
<div class="abs f-text" style="left:0;top:3713px;width:1200px;text-align:center;font-size:15px">Copyrights@2024.Company Name.All Rights Reserved</div>

</body>
</html>
```